Revamp Marketing Website For Video Production Website

need to revamp current website www.quillhavenfilmworks.com
reference sites www.vandeo.com & http://layoutpike.com/quill/
Use all current content on current quill website. I want a revamped modenr look. Sometbing that wows customers.
reference site www.vandeo.com
Target Market(s)
business owners
Industry/Entity Type
Video Production
Number of Pages Required
5+ page
Colors
Designer to choose colors to be used in the design.
Requirements
Must have
- need to revamp current website www.quillhavenfilmworks.com
- reference sites www.vandeo.com & http://layoutpike.com/quill/
- Use all current content on current quill website. I want a revamped modenr look. Sometbing that wows customers.
- reference site www.vandeo.com
Nice to have
Should not have

```html
<!DOCTYPE html>
<html lang="en">
<head>
<meta charset="utf-8">
<title>Quill — Marketing Videos Made For You</title>
<link rel="stylesheet" href="https://fonts.googleapis.com/css2?family=Montserrat:wght@400;500;600;700&family=Open+Sans:wght@400;600;700&display=swap">
<style>
:root{
  --brand:#0ea5dd;
  --brand-deep:#0b87bf;
  --ink:#1d1d1f;
  --ink-soft:#444;
  --muted:#666;
  --grey-band:#e6e6e6;
  --white:#fff;
}
*{margin:0;padding:0;box-sizing:border-box}
html,body{width:1200px;height:1200px;overflow:hidden;background:var(--white)}
body{position:relative;font-family:"Open Sans",sans-serif;color:var(--ink)}
.page{position:absolute;left:421.7px;top:0;width:574px;height:1932px;transform:scale(.6211);transform-origin:0 0;background:var(--white);box-shadow:0 0 40px rgba(0,0,0,.12);overflow:hidden}
.abs{position:absolute}
.head{font-family:"Montserrat",sans-serif}
.btn{position:absolute;display:flex;align-items:center;justify-content:center;border-radius:10px;background:var(--brand);color:var(--white);font-family:"Montserrat",sans-serif;font-size:5.5px;font-weight:500}
.btn-outline{background:transparent;border:1px solid var(--brand);color:var(--brand)}
.photo{position:absolute}

/* nav */
.nav{position:absolute;left:0;top:0;width:574px;height:31px;background:var(--white)}
.logo{position:absolute;display:flex;align-items:center;gap:4px;font-family:"Montserrat",sans-serif;font-weight:700;letter-spacing:3px}
.logo-mark{width:9px;height:9px;background:var(--brand)}
.logo-tag{position:absolute;font-family:"Montserrat",sans-serif;font-size:3.6px;letter-spacing:.6px}
.nav-link{position:absolute;top:14px;font-family:"Montserrat",sans-serif;font-size:5.2px;color:var(--ink-soft)}
.nav-link.active{color:var(--brand);font-weight:600}

/* hero */
.hero{position:absolute;left:0;top:31px;width:574px;height:292px;background:
  radial-gradient(ellipse at 72% 35%,rgba(232,70,100,.85) 0%,rgba(180,40,90,.4) 30%,transparent 55%),
  radial-gradient(ellipse at 20% 75%,rgba(40,90,220,.9) 0%,transparent 50%),
  linear-gradient(135deg,#0d1f5a 0%,#14296e 45%,#5a1f4e 75%,#1a1e4e 100%)}
.hero-text{position:absolute;left:0;width:574px;text-align:center;color:var(--white);font-family:"Montserrat",sans-serif}

/* promote */
.h-title{font-family:"Montserrat",sans-serif;font-weight:700;font-size:11.5px;color:var(--ink)}
.h-sub{font-family:"Montserrat",sans-serif;font-weight:600;font-size:9.5px;color:var(--ink-soft)}
.body-copy{font-size:5.3px;line-height:9px;color:var(--muted)}

.network-grid{position:absolute;left:42px;top:508px;width:222px;display:grid;grid-template-columns:repeat(4,auto);gap:14px 8px;font-family:"Montserrat",sans-serif;font-weight:700;color:var(--brand);font-size:10.5px}

/* examples */
.examples{position:absolute;left:0;top:657px;width:574px;height:206px;background:var(--brand)}
.thumb-cap{position:absolute;width:160px;text-align:center;top:169px;color:var(--white);font-family:"Montserrat",sans-serif;font-size:6.5px}

/* facts */
.fact-num{position:absolute;font-family:"Montserrat",sans-serif;font-weight:300;font-size:24px;color:var(--brand);line-height:1}
.fact{position:absolute;width:145px}
.fact-head{font-family:"Montserrat",sans-serif;font-weight:600;font-size:6.3px;line-height:9.6px;color:var(--ink)}
.fact-body{margin-top:3px;font-size:5.2px;line-height:9px;color:var(--muted)}

/* sizes */
.sizes{position:absolute;left:0;top:1208px;width:574px;height:636px;background:var(--grey-band)}
.center{position:absolute;left:0;width:574px;text-align:center}
.size-label{font-family:"Montserrat",sans-serif;font-weight:600;font-size:6.8px;color:var(--ink-soft)}
.size-desc{font-size:5.2px;line-height:9px;color:var(--muted)}
.size-desc b{color:var(--ink)}

/* footer */
.footer{position:absolute;left:0;top:1844px;width:574px;height:88px;background:var(--brand-deep);color:var(--white)}
.foot-link{position:absolute;top:67px;font-family:"Montserrat",sans-serif;font-size:5.2px}
</style>
</head>
<body>
<div class="page">

  <header class="nav">
    <div class="logo" style="left:42px;top:7px;font-size:12px;color:#555"><span class="logo-mark"></span>QUILL</div>
    <div class="logo-tag" style="left:42px;top:22px;color:#999">MARKETING VIDEOS MADE FOR YOU</div>
    <span class="nav-link active" style="left:166px">Home</span>
    <span class="nav-link" style="left:194px">How it works</span>
    <span class="nav-link" style="left:241px">Examples</span>
    <span class="nav-link" style="left:279px">Faq</span>
    <span class="nav-link" style="left:301px">Pricing</span>
    <span class="nav-link" style="left:332px">Contact Us</span>
    <span class="nav-link" style="left:455px">LOGIN</span>
    <span class="btn btn-outline" style="left:480px;top:12px;width:52px;height:11px;font-size:5px">SIGN UP</span>
  </header>

  <section class="hero" role="img" aria-label="Close-up of a professional film camera in blue and red light">
    <div class="hero-text" style="top:100px;font-size:10.5px">WE CREATE <b>ATTENTION GRABBING</b></div>
    <div class="hero-text" style="top:116px;font-size:21px">"<b>VIRAL</b>" TYPE VIDEO ADS</div>
    <div class="hero-text" style="top:153px;font-size:7.3px">THE FIRST MOCKUP IS ON US! NO PURCHASE NECESSARY.</div>
    <span class="btn" style="left:246px;top:173px;width:82px;height:17px">GET FREE MOCKUP</span>
  </section>

  <section>
    <div class="h-title abs" style="left:42px;top:360px">Promote anything.</div>
    <div class="h-sub abs" style="left:42px;top:377px">Anywhere on the web.</div>
    <p class="body-copy abs" style="left:42px;top:397px;width:200px">Still using static image ads with Friendline, Glimpse, Worknet, Blinkchat advertising platforms? Turn them into VIDEO ADS and get higher conversion rates instantly!</p>
    <span class="btn" style="left:42px;top:433px;width:83px;height:18px">GET YOUR VIDEO</span>
    <div class="photo" role="img" aria-label="Film crew holding a clapperboard in front of a camera" style="left:289px;top:360px;width:243px;height:119px;background:linear-gradient(120deg,#2a2c30 0%,#4a4a4e 40%,#b9a28c 70%,#9a6c50 100%)"></div>

    <div class="network-grid">
      <span>Friendline</span><span>Glimpse</span><span>Chirpy</span><span>Streamly</span>
      <span>Pinboardly</span><span>Reelhub</span><span>Worknet</span><span>Circles</span>
    </div>

    <div class="h-title abs" style="left:331px;top:511px">We Create.</div>
    <div class="h-sub abs" style="left:331px;top:528px;width:200px;font-size:8.8px;line-height:13px">Award Winning Promotional Marketing Videos To Use All Over The Web.</div>
    <p class="body-copy abs" style="left:331px;top:561px;width:202px">Lorem ipsum dolor sit amet consectetur adipiscing elit sed do eiusmod tempor incididunt ut labore. Dolore magna aliqua ut enim ad minim veniam quis nostrud exercitation ullamco laboris nisi. Aliquip ex ea commodo consequat duis aute irure dolor. In reprehenderit in voluptate velit esse cillum dolore eu fugiat nulla pariatur, excepteur sint occaecat cupidatat non proident sunt culpa.</p>
  </section>

  <section class="examples">
    <div class="abs head" style="left:42px;top:9px;font-weight:700;font-size:11.5px;color:var(--white)">Our Examples.</div>
    <div class="abs head" style="left:42px;top:25px;font-weight:600;font-size:9px;color:var(--white)">Take a glance at our previous work</div>
    <span class="btn btn-outline" style="left:42px;top:45px;width:82px;height:17px;border-color:var(--white);color:var(--white);font-size:5px">MARKETING ▾</span>
    <div class="photo" role="img" aria-label="Video still: man in a suit outside a glass office building" style="left:42px;top:73px;width:160px;height:91px;background:linear-gradient(160deg,#5d7fa8,#2e3e5a 70%,#8a5a50)"></div>
    <div class="photo" role="img" aria-label="Video still: businessman throwing money against a concrete wall" style="left:207px;top:73px;width:160px;height:91px;background:linear-gradient(160deg,#8a8e92,#4d5257 60%,#2c2f33)"></div>
    <div class="photo" role="img" aria-label="Video still: man in a pink tutu in a dance studio" style="left:372px;top:73px;width:160px;height:91px;background:linear-gradient(180deg,#eceae6,#d8cfc8 60%,#e07a92)"></div>
    <span class="thumb-cap" style="left:42px">VIDEO TITLE #1</span>
    <span class="thumb-cap" style="left:207px">VIDEO TITLE #2</span>
    <span class="thumb-cap" style="left:372px">VIDEO TITLE #3</span>
  </section>

  <section>
    <div class="center head" style="top:892px;font-weight:700;font-size:11.5px">6 Facts</div>
    <div class="center head" style="top:909px;font-weight:600;font-size:9px;color:var(--ink-soft)">Why we are the best for you?</div>

    <span class="fact-num" style="left:55px;top:956px">1</span>
    <div class="fact" style="left:66px;top:955px"><div class="fact-head">DONE FOR YOU.<br>YOU DON'T LIFT A FINGER!</div><p class="fact-body">We make it super affordable and we DO IT ALL FOR YOU. You'll receive a fully packaged, professionally edited and designed video all delivered within 24 hours!</p></div>

    <span class="fact-num" style="left:209px;top:955px">2</span>
    <div class="fact" style="left:226px;top:954px"><div class="fact-head">PREMIUM CONTENT.<br>YOUR BUSINESS WILL LOOK<br>SUPER HIGH END &amp; PROFESSIONAL!</div><p class="fact-body">We have access to millions of premium video clips, fully packaged by Award Winning Videographers, professionally edited and hand picked music to create the most stunning marketing videos for our clients.</p></div>

    <span class="fact-num" style="left:381px;top:955px">3</span>
    <div class="fact" style="left:398px;top:954px;width:136px"><div class="fact-head">FULLY LICENSED TO YOU.<br>YOU OWN ALL THE VIDEOS TO USE FOREVER - CONSIDER THEM ASSETS!</div><p class="fact-body">The videos are your property and come with a lifetime license for unlimited sharing and use. The videos you make are yours to post online anywhere, anytime and forever. You own them outright 100%.</p></div>

    <span class="fact-num" style="left:52px;top:1061px">4</span>
    <div class="fact" style="left:68px;top:1060px"><div class="fact-head">PERFECT LENGTH.<br>STAND OUT FROM THE CROWD<br>WITH VIDEO MARKETING!</div><p class="fact-body">Our Marketing Videos range from 10 seconds up to 30 seconds in length. These are the recommended length and widely accepted on most advertising platforms. Blinkchat, however, only allows for 10 second video length on their advertising platform.</p></div>

    <span class="fact-num" style="left:217px;top:1060px">5</span>
    <div class="fact" style="left:233px;top:1059px"><div class="fact-head">BEST SUPPORT.<br>WE ARE AVAILABLE TO YOU AT<br>ALL TIMES FOR ANY KIND OF SUPPORT</div><p class="fact-body">Reach out anytime, anywhere. Our team of tech, marketing and video experts are here to help you grow your business. Email us at support@quillhavenfilmworks.com</p></div>

    <span class="fact-num" style="left:374px;top:1058px">6</span>
    <div class="fact" style="left:391px;top:1057px;width:145px"><div class="fact-head">FRIENDLINE VIDEO COVER<br>"WOW" CUSTOMERS WITH A BEAUTIFUL DESIGNED FRIENDLINE COVER VIDEO!</div><p class="fact-body">We can convert any video to a Friendline Video Cover for your FL Business page.</p></div>

    <span class="btn" style="left:246px;top:1164px;width:82px;height:17px">VIEW MORE</span>
  </section>

  <section class="sizes">
    <div class="center head" style="top:28px;font-weight:700;font-size:11.5px">Video sizes available</div>
    <div class="center head" style="top:45px;font-weight:600;font-size:9px;color:var(--ink-soft)">We do it all.</div>

    <div class="center size-label" style="top:73px">Wide Screen Videos</div>
    <div class="center size-desc" style="top:82px;padding:0 130px">This size is a standard video size that works best for pretty much anywhere on the web (1080x720). <b>Included with all video purchases.</b></div>
    <div class="photo" role="img" aria-label="Chef plating food from a pan" style="left:42px;top:108px;width:119px;height:69px;background:linear-gradient(135deg,#f2f0ee,#b9b3ad 60%,#5a4a40)"></div>
    <div class="photo" role="img" aria-label="Man on a park bench using a phone" style="left:166px;top:108px;width:118px;height:69px;background:linear-gradient(135deg,#9cc46a,#c9b89c 55%,#5a4e44)"></div>
    <div class="photo" role="img" aria-label="Couple looking at a tablet together" style="left:289px;top:108px;width:119px;height:69px;background:linear-gradient(135deg,#e8e2da,#c8a890 55%,#6a5a50)"></div>
    <div class="photo" role="img" aria-label="Gourmet burgers on a table" style="left:413px;top:108px;width:119px;height:69px;background:linear-gradient(135deg,#3b2b22,#a0622e 50%,#5c7a2e)"></div>

    <div class="center size-label" style="top:200px">Square Videos</div>
    <div class="center size-desc" style="top:209px">Work best on FRIENDLINE (Square is 1080 X 1080)<br><b>Convert any video</b> to this size for an additional <b>fee of $39.</b></div>
    <div class="photo" role="img" aria-label="Grocer handing a paper bag to a customer" style="left:42px;top:235px;width:119px;height:118px;background:linear-gradient(135deg,#d9a05a,#efe6da 55%,#3a3a40)"></div>
    <div class="photo" role="img" aria-label="Glowing vintage light bulbs in the dark" style="left:166px;top:235px;width:118px;height:118px;background:radial-gradient(circle at 50% 45%,#f0a040 0%,#8a4a10 25%,#0c0806 60%)"></div>
    <div class="photo" role="img" aria-label="Large brick house with a gravel driveway" style="left:289px;top:235px;width:119px;height:118px;background:linear-gradient(180deg,#6a9a5a,#9c7a6a 50%,#a89c90)"></div>
    <div class="photo" role="img" aria-label="Light bulb lying on a pale surface" style="left:413px;top:235px;width:119px;height:118px;background:radial-gradient(circle at 55% 55%,#f2e6c8 0%,#a8d0cc 45%,#5e9ea6 100%)"></div>

    <div class="center size-label" style="top:378px">Vertical Videos</div>
    <div class="center size-desc" style="top:387px">Work best on STORIES for Friendline, Glimpse and Blinkchat (1080 X 1920)<br><b>Convert any video</b> to this size for an additional <b>fee of $39.</b></div>
    <div class="photo" role="img" aria-label="Woman with shopping bags on a city street" style="left:42px;top:413px;width:119px;height:197px;background:linear-gradient(180deg,#b89a7a,#6a4a3a 50%,#d8d4cc)"></div>
    <div class="photo" role="img" aria-label="Woman smiling at her phone outdoors" style="left:166px;top:413px;width:118px;height:197px;background:linear-gradient(180deg,#7aa86a,#6a4a3a 45%,#e8e6ea)"></div>
    <div class="photo" role="img" aria-label="Football player in uniform on the field" style="left:289px;top:413px;width:119px;height:197px;background:linear-gradient(180deg,#9a9a92,#1e2a48 45%,#6a8a4a)"></div>
    <div class="photo" role="img" aria-label="Woman cheering on a sunny street" style="left:413px;top:413px;width:119px;height:197px;background:linear-gradient(180deg,#e8c890,#b88a5a 45%,#efeae2)"></div>
  </section>

  <footer class="footer">
    <div class="logo" style="left:42px;top:8px;font-size:12px;color:var(--white)"><span class="logo-mark" style="background:var(--white)"></span>QUILL</div>
    <div class="logo-tag" style="left:42px;top:23px;color:var(--white)">MARKETING VIDEOS MADE FOR YOU</div>
    <div class="abs head" style="left:42px;top:37px;font-size:5.4px;font-weight:700">CREATED BY A MARKETER FOR MARKETERS</div>
    <p class="abs" style="left:42px;top:52px;width:165px;font-size:4.6px;line-height:9px">With Quill, you simply let us know what you want to promote and we will have your video ad finished as soon as 24 hours!</p>
    <div class="abs head" style="left:464px;top:9px;font-size:5px;font-weight:700">FOLLOW US:</div>
    <div class="abs head" style="left:464px;top:20px;font-size:4.4px;font-weight:600;width:80px;line-height:6px">Friendline · Chirpy · Worknet · Streamly · Circles</div>
    <span class="foot-link" style="left:337px">Home</span>
    <span class="foot-link" style="left:365px">How it works</span>
    <span class="foot-link" style="left:412px">Examples</span>
    <span class="foot-link" style="left:450px">Faq</span>
    <span class="foot-link" style="left:472px">Pricing</span>
    <span class="foot-link" style="left:503px">Contact Us</span>
  </footer>

</div>
</body>
</html>
```